meridale partners business card

Architectural firm business card
Updates

Please note:

corporate colour black+yellow are the only elements to be kept.
NO OTHER ELEMENT TO BE REUSED FROM PREVIOUS BUSINESS CARD.
Thank you.

Dear Everyone,

Thank you for your participation. I have upload the KBSO+ logo again for incoporate in the card. in tif and pdf format.

Thank you 

I keep getting request for the logo file. Does everyone has the same problem?

I cannot do much, because the file is upload to the website server. I can't seem to see it either.

The logo file is now working. Please download. I check it myself. Thank you everyone.

Dear All,

Thank you for all the hard work. There are a lot of great work. Due to current commitment with work, I am unable to review them just yet. I will do so next week and advise everyone also. Thank you again. Best regards

Dear All,

Thank you for your participation. There are a lot of good design. Unfortunately, I can only select one. All the best. This is definitely a good crowd to work with. Thank you everyone again.

Best regards

Target Market(s)

Corporate, commercial and institutional projects only

Industry/Entity Type

Business

Requirements
Must have
• elegant simple
double sided with coating
Member of Southland Guild of Draughtsmen (logo only)
corporate colour black and

LOGO FILE UPLOADED
Should not have
• should not be the same as current business card.
upload for reference information only.
font sans serif preferred.

```html
<!DOCTYPE html>
<html lang="en">
<head>
<meta charset="utf-8">
<title>Meridale Partners business card</title>
<link href="https://fonts.googleapis.com/css2?family=PT+Sans:wght@400;700&family=PT+Sans+Narrow:wght@400;700&display=swap" rel="stylesheet">
<style>
  :root {
    --page: #e6e6e6;
    --card: #3c3c3e;
    --card-edge: #2e2e30;
    --orange: #f58220;
    --white: #ffffff;
    --muted: #b9b9bb;
    --ink: #3a3a3c;
  }
  * { margin: 0; padding: 0; box-sizing: border-box; }
  html, body { width: 1200px; height: 646px; overflow: hidden; }
  body {
    background: radial-gradient(ellipse at 30% 30%, #f7f7f7, var(--page));
    font-family: "PT Sans", Arial, sans-serif;
    position: relative;
  }
  .card {
    position: absolute;
    top: 163px;
    width: 560px;
    height: 320px;
    background: var(--card);
    box-shadow: 0 10px 28px rgba(0,0,0,.28);
    overflow: hidden;
  }
  .card--front { left: 27px; }
  .card--back { left: 613px; }

  /* front */
  .front-band { position: absolute; left: 0; top: 112px; }
  .front-brand {
    position: absolute; left: 150px; top: 122px;
    display: flex; align-items: center; gap: 12px;
  }
  .brand-square { width: 26px; height: 26px; background: var(--ink); }
  .front-brand .brand-name {
    font-family: "PT Sans Narrow", Arial, sans-serif;
    font-weight: 700; font-size: 28px; color: var(--ink); letter-spacing: .5px;
  }
  .services {
    position: absolute; left: 150px; top: 178px;
    list-style: none; color: var(--orange); font-size: 17px; line-height: 19px;
  }

  /* back */
  .person { position: absolute; left: 32px; top: 150px; }
  .person-name { font-size: 26px; font-weight: 700; color: var(--orange); }
  .person-name .role { font-weight: 400; color: var(--muted); font-size: 20px; margin-left: 6px; }
  .person-creds { color: var(--white); font-size: 12px; margin-top: 2px; }
  .person-mobile { color: var(--muted); font-size: 18px; font-weight: 700; margin-top: 2px; }

  .contact-tab { position: absolute; right: 0; top: 26px; }
  .contact-list {
    position: absolute; right: 70px; top: 38px;
    list-style: none; text-align: right; color: var(--white);
    font-size: 13.5px; line-height: 25px;
  }
  .contact-list .address-head { font-weight: 700; margin-top: 6px; }

  .back-brand {
    position: absolute; left: 32px; bottom: 26px;
    display: flex; align-items: center; gap: 10px;
  }
  .back-brand .brand-square { background: var(--orange); width: 20px; height: 20px; }
  .back-brand .brand-name {
    font-family: "PT Sans Narrow", Arial, sans-serif;
    font-weight: 700; font-size: 24px; color: var(--white); letter-spacing: .5px;
  }
</style>
</head>
<body>

<section class="card card--front" aria-label="Card front">
  <svg class="front-band" width="560" height="56" viewBox="0 0 560 56" aria-hidden="true">
    <polygon points="0,0 518,0 540,28 518,56 0,56" fill="var(--orange)"/>
  </svg>
  <div class="front-brand">
    <span class="brand-square"></span>
    <span class="brand-name">Meridale Partners</span>
  </div>
  <ul class="services">
    <li>architects</li>
    <li>urban designers</li>
    <li>project managers</li>
  </ul>
</section>

<section class="card card--back" aria-label="Card back">
  <svg class="contact-tab" width="60" height="176" viewBox="0 0 60 176" aria-hidden="true">
    <path d="M60,0 H30 A30,30 0 0 0 0,30 V146 A30,30 0 0 0 30,176 H60 Z" fill="var(--orange)"/>
    <g fill="var(--white)" stroke="none">
      <!-- phone -->
      <path d="M22,14 q-3,2 0,7 q4,6 9,8 q4,1 5,-2 l-3,-3 q-2,1 -3,0 q-3,-2 -4,-5 q0,-1 1,-2 z"/>
      <!-- fax -->
      <rect x="21" y="45" width="16" height="12" rx="1"/>
      <rect x="24" y="40" width="10" height="6" fill="var(--orange)" stroke="var(--white)" stroke-width="1.5"/>
      <!-- mail -->
      <rect x="20" y="70" width="18" height="12" rx="1"/>
      <path d="M20,70 L29,77 L38,70" fill="none" stroke="var(--orange)" stroke-width="1.5"/>
      <!-- globe -->
      <circle cx="29" cy="102" r="9"/>
      <g fill="none" stroke="var(--orange)" stroke-width="1.2">
        <ellipse cx="29" cy="102" rx="4" ry="9"/>
        <line x1="20" y1="102" x2="38" y2="102"/>
      </g>
      <!-- home -->
      <path d="M29,119 L39,128 H36 V137 H22 V128 H19 Z"/>
    </g>
  </svg>
  <ul class="contact-list">
    <li>+612 9410 2273</li>
    <li>+612 9410 2274</li>
    <li>mail@meridalepartners.com.au</li>
    <li>www.meridalepartners.com.au</li>
    <li class="address-head">Calloway House</li>
    <li>12 Fenwick St, Ashgrove NSW 2170</li>
  </ul>

  <div class="person">
    <p class="person-name">Linh Harper<span class="role">Director</span></p>
    <p class="person-creds">kbso, sgd, Architect (NSW BoA reg. no: 3172)</p>
    <p class="person-mobile">M 0412 706 384</p>
  </div>

  <div class="back-brand">
    <span class="brand-square"></span>
    <span class="brand-name">Meridale Partners</span>
  </div>
</section>

</body>
</html>
```